tarnu

We are a group of companies that we want to make a triptych. we want the general information of the work we do and the information of each company with its logo

```html
<!DOCTYPE html>
<html lang="es">
<head>
<meta charset="utf-8">
<title>Power Team Nexo Tarnu – Tríptico</title>
<link href="https://fonts.googleapis.com/css2?family=EB+Garamond:wght@400;500&display=swap" rel="stylesheet">
<style>
:root{
  --backdrop:#6c6b6f;
  --paper:#ffffff;
  --pink:#e4506a;
  --ink:#1d1d1b;
  --black:#000000;
  --yellow:#fef27a;
  --orange:#e9502f;
  --rule:#8a8a8a;
}
*{margin:0;padding:0;box-sizing:border-box}
html,body{width:1108px;height:1200px;overflow:hidden}
body{background:var(--backdrop);font-family:"EB Garamond",Georgia,serif;color:var(--ink);position:relative}
h1,h2{font-weight:400}
.sheet{position:absolute;left:171px;width:765px;height:447px;background:var(--paper);display:grid;grid-template-columns:255px 255px 255px}
.sheet--outside{top:115px}
.sheet--inside{top:638px;grid-template-rows:167px 280px}

/* company name stand-ins */
.brand{font-family:"EB Garamond",Georgia,serif;font-weight:500;font-size:15px;color:var(--ink);display:flex;align-items:center;gap:6px;white-space:nowrap}
.brand__mark{width:9px;height:9px;background:var(--pink)}

/* outside sheet */
.logo-column{background:linear-gradient(#e9eaea,#fafafa);padding:12px 26px;display:flex;flex-direction:column}
.logo-column .logo-slot{flex:1;display:flex;align-items:center;justify-content:center;border-bottom:1px dotted var(--rule)}
.logo-column .logo-slot:last-child{border-bottom:none}

.service-panel{display:flex;flex-direction:column;border-left:1px solid #ddd}
.service-panel__title{background:var(--pink);color:#fff;font-size:19px;line-height:19px;text-align:center;padding:9px 6px 0;height:55px}
.service-list{list-style:none;padding:7px 29px 0}
.service-list li{font-size:7.4px;line-height:8.1px;text-align:center;padding:2.6px 0 2.7px;border-bottom:1px solid var(--pink)}
.service-list li:last-child{border-bottom:none}

.cover{display:flex;flex-direction:column}
.cover__name{background:var(--black);color:#fff;height:331px;display:flex;flex-direction:column;justify-content:center;align-items:center;font-size:48px;line-height:56px;letter-spacing:1px}
.cover__tag{background:var(--pink);color:#fff;flex:1;display:flex;align-items:center;justify-content:center;text-align:center;font-size:18px;line-height:23px;letter-spacing:.5px}

/* inside sheet */
.partner-grid{grid-column:1/3;background:linear-gradient(#e6e7e7,#f6f6f6);position:relative;display:grid;grid-template-columns:1fr 1fr;grid-template-rows:1fr 1fr;padding:14px 50px}
.partner-grid .logo-slot{display:flex;align-items:center;justify-content:center}
.partner-grid::before{content:"";position:absolute;left:50px;right:50px;top:84px;border-top:1px dotted var(--rule)}
.partner-grid::after{content:"";position:absolute;left:255px;top:28px;bottom:28px;border-left:1px dotted var(--rule)}

.side-column{grid-column:3;grid-row:1/3;display:flex;flex-direction:column}
.side-logos{height:167px;padding:18px 84px 14px;display:flex;flex-direction:column}
.side-logos .logo-slot{flex:1;display:flex;align-items:center;justify-content:center;border-bottom:1px dotted var(--ink)}
.side-logos .logo-slot:last-child{border-bottom:none}
.side-column .service-panel{border-left:none}
.side-column .service-panel__title{height:56px;padding-top:10px}
.side-column .service-list{padding:22px 43px 0}
.side-column .service-list li{padding:4.4px 0 4.5px}

.project-intro{background:var(--yellow);display:flex;align-items:center;justify-content:center;text-align:center;font-size:18px;line-height:34px;padding-bottom:12px}
.project-list{background:var(--yellow);border-left:1px solid #e4d960;list-style:none;padding:21px 35px 0 35px}
.project-list li{background:var(--orange);color:#fff;font-size:8.6px;line-height:10.4px;text-align:center;padding:1.5px 6px;margin-bottom:6px}
</style>
</head>
<body>

<section class="sheet sheet--outside">
  <div class="logo-column">
    <div class="logo-slot"><span class="brand"><span class="brand__mark"></span>Forma Studio</span></div>
    <div class="logo-slot"><span class="brand">Carpinterías Orlan</span></div>
    <div class="logo-slot"><span class="brand">Mevra SL</span></div>
    <div class="logo-slot"><span class="brand">Dalmo Interiorisme</span></div>
    <div class="logo-slot"><span class="brand"><span class="brand__mark"></span>Velter</span></div>
    <div class="logo-slot"><span class="brand">Norvi Group</span></div>
    <div class="logo-slot"><span class="brand"><span class="brand__mark"></span>Ferral Arquitectes</span></div>
  </div>

  <div class="service-panel">
    <h2 class="service-panel__title">CONSTRUCCIÓN Y OBRA<br>PARA PARTICULARES</h2>
    <ul class="service-list">
      <li>Pintura de viviendas y aparcamientos en edificios de viviendas</li>
      <li>Pintura de protección de elementos especiales</li>
      <li>Falsos techos registrables y fijos</li>
      <li>Construcción y reforma de cubiertas, planas o inclinadas, transitables o técnicas, en viviendas y edificios de viviendas</li>
      <li>Impermeabilización y aislamiento térmico, acústico y estanco en viviendas nuevas y a rehabilitar o reformar</li>
      <li>Impermeabilización de medianeras mediante tabiques pluviales de diferentes tipos</li>
      <li>Instalación y mantenimiento de calefacción por aire y radiador</li>
      <li>Instalación y mantenimiento de climatización por aire</li>
      <li>Alicatados en cocinas y baños</li>
      <li>Chapados y revestimientos en viviendas y zonas comunes de edificios de viviendas</li>
      <li>Pavimentos de madera, cerámica y piedra en viviendas y zonas comunes de viviendas</li>
      <li>Carpintería de madera en interiores de viviendas</li>
      <li>Carpintería de aluminio en viviendas y edificios de viviendas</li>
      <li>Instalación y mantenimiento de electricidad y domótica</li>
      <li>Instalación y mantenimiento de sistemas de alumbrado, tanto en interiores como en exteriores</li>
      <li>Instalación y mantenimiento de alumbrado de emergencia en zonas comunes de edificios de viviendas</li>
      <li>Instalación y mantenimiento de instalación de fontanería y saneamiento</li>
      <li>Instalación de ascensores especiales para viviendas</li>
      <li>Instalación y mantenimiento de instalaciones de protección contra incendios en aparcamientos de viviendas unifamiliares, aparcamientos de edificios de viviendas y zonas comunes de edificios de viviendas</li>
    </ul>
  </div>

  <div class="cover">
    <h1 class="cover__name"><span>POWER</span><span>TEAM</span><span>NEXO</span><span>TARNU</span></h1>
    <p class="cover__tag">GRUPO DE<br>CONSTRUCTIÓN</p>
  </div>
</section>

<section class="sheet sheet--inside">
  <div class="partner-grid">
    <div class="logo-slot"><span class="brand"><span class="brand__mark"></span>Ferral Arquitectes</span></div>
    <div class="logo-slot"><span class="brand"><span class="brand__mark"></span>Forma Studio</span></div>
    <div class="logo-slot"><span class="brand">Norvi Group</span></div>
    <div class="logo-slot"><span class="brand"><span class="brand__mark"></span>Velter</span></div>
  </div>

  <div class="side-column">
    <div class="side-logos">
      <div class="logo-slot"><span class="brand">Mevra SL</span></div>
      <div class="logo-slot"><span class="brand">Dalmo Interiorisme</span></div>
      <div class="logo-slot"><span class="brand">Carpinterías Orlan</span></div>
    </div>
    <div class="service-panel">
      <h2 class="service-panel__title">CONSTRUCCIÓN Y OBRA<br>PARA PARTICULARES</h2>
      <ul class="service-list">
        <li>Derribo de construcciones</li>
        <li>Excavación y movimiento de tierras</li>
        <li>Cimentaciones de viviendas</li>
        <li>Estructuras de hormigón, acero y madera para viviendas nuevas</li>
        <li>Refuerzo y reparación de estructuras de hormigón, acero y madera para rehabilitación y/o re-forma de viviendas</li>
        <li>Diseño y construcción de mobiliario a medida</li>
        <li>Diseño y construcción de cocinas a medida de la marca Olmeda</li>
        <li>Reforma y rehabilitación de cocinas y baños</li>
        <li>Albañilería tradicional de ladrillo y tabiquería en seco tipo Placarel</li>
      </ul>
    </div>
  </div>

  <h2 class="project-intro">DISEÑO Y<br>GESTIÓN DE<br>PROYECTOS Y<br>OBRAS PARA<br>PARTICULARES</h2>

  <ul class="project-list">
    <li>Proyecto de obra nueva</li>
    <li>Proyecto de reforma y rehabilitación</li>
    <li>Proyecto de interiorismo y decoración</li>
    <li>Proyecto de cambio de uso de locales comerciales y oficinas a vivienda</li>
    <li>Proyecto de legalización de viviendas y otras construcciones</li>
    <li>Tramitación de licencia de obras ante ayuntamientos y administraciones equivalentes</li>
    <li>Dirección de obra</li>
    <li>Comercialización y valoración de inmuebles, tanto para clientes nacionales como extranjeros que busquen propiedades en España, con especial énfasis en viviendas de alto standing en zonas costeras</li>
  </ul>
</section>

</body>
</html>
```